The maple crew

I want it as prefession and attractive as possible we are a lawnmowing business

Phone number 605-318-2264
Name- Carlos Whitfield
Email- themaplecrewsd@fernpost.com

```html
<!DOCTYPE html>
<html lang="en">
<head>
<meta charset="utf-8">
<title>The maple crew – business cards</title>
<link href="https://fonts.googleapis.com/css2?family=Saira:wght@700;800&family=Montserrat:wght@500&display=swap" rel="stylesheet">
<style>
  :root {
    --backdrop: #1f1f20;
    --card: #ffffff;
    --green-dark: #0a5e3a;
    --green-deep: #084a2e;
    --green-light: #5cb947;
    --ink-light: #ffffff;
  }
  * { box-sizing: border-box; margin: 0; padding: 0; }
  html, body {
    width: 1200px; height: 795px; overflow: hidden;
    background: var(--backdrop);
  }
  .canvas {
    position: relative; width: 1200px; height: 795px;
    display: flex; align-items: center; justify-content: center; gap: 40px;
  }
  .card {
    position: relative; width: 540px; height: 309px;
    background: var(--card); overflow: hidden;
    box-shadow: 0 18px 40px rgba(0,0,0,.45);
  }

  /* Front: brand mark */
  .card-front { display: flex; align-items: center; justify-content: center; }
  .brand { display: flex; align-items: center; gap: 14px; }
  .brand-square { width: 22px; height: 22px; background: var(--green-dark); }
  .brand-name {
    font-family: "Saira", sans-serif; font-weight: 800;
    font-size: 44px; letter-spacing: 1px; text-transform: uppercase;
    color: var(--green-dark); line-height: 1;
  }

  /* Back: contact details */
  .band-top {
    position: absolute; left: 0; top: 0; width: 100%; height: 36px;
    background: var(--green-dark);
  }
  .holder-name {
    position: absolute; left: 26px; top: 62px;
    font-family: "Saira", sans-serif; font-weight: 700;
    font-size: 30px; letter-spacing: 1px; text-transform: uppercase;
    color: var(--green-dark);
  }
  .band-bottom {
    position: absolute; left: 0; top: 192px; width: 100%; height: 117px;
    background: var(--green-dark);
  }
  .scene-art {
    position: absolute; left: 330px; top: 118px; width: 190px; height: 86px;
    background: linear-gradient(180deg, var(--green-dark) 0%, var(--green-deep) 100%);
    border-radius: 40px 40px 0 0;
  }
  .contact {
    position: absolute; display: flex; align-items: center; gap: 10px;
    font-family: "Montserrat", sans-serif; font-weight: 500;
    font-size: 13px; letter-spacing: .4px; color: var(--ink-light);
  }
  .contact-phone { left: 26px; top: 220px; }
  .contact-email { right: 26px; top: 270px; }
  .contact-icon { width: 18px; height: 18px; flex: none; }
</style>
</head>
<body>
<main class="canvas">

  <section class="card card-front" aria-label="Card front">
    <div class="brand">
      <span class="brand-square"></span>
      <span class="brand-name">The maple crew</span>
    </div>
  </section>

  <section class="card card-back" aria-label="Card back">
    <div class="band-top"></div>
    <h1 class="holder-name">Carlos Whitfield</h1>
    <div class="band-bottom"></div>
    <div class="scene-art" role="img" aria-label="Silhouette of a worker pushing a lawn mower through tall grass"></div>

    <p class="contact contact-phone">
      <svg class="contact-icon" viewBox="0 0 20 20" aria-hidden="true">
        <circle cx="10" cy="10" r="10" fill="#ffffff"/>
        <path d="M7.2 5.2l1.6 2.4-1 1.2c.6 1.3 1.5 2.2 2.8 2.8l1.2-1 2.4 1.6-.7 1.9c-4.2-.3-7.6-3.7-7.9-7.9z" fill="var(--green-dark)"/>
      </svg>
      605-318-2264
    </p>

    <p class="contact contact-email">
      <svg class="contact-icon" viewBox="0 0 20 20" aria-hidden="true">
        <circle cx="10" cy="10" r="10" fill="#ffffff"/>
        <text x="10" y="14" text-anchor="middle" font-family="Montserrat, sans-serif" font-size="12" font-weight="500" fill="var(--green-dark)">@</text>
      </svg>
      themaplecrewsd@fernpost.com
    </p>
  </section>

</main>
</body>
</html>
```